Business card design for online Mandarin Learning School

We need a business card design for our online language learning school called "Maple Bridge Online for Mandarin Learning". Our existing website is https://www.maplebridgeonline.com
We have our logo already. We would like to see our business card design that can make our online teaching services to be innovative, young, energetic and fun to learn. Prefer to have a certain level of color matching with our website. Apart from "Maple Bridge Online", need to specifically state "for Mandarin Learning" as well on the business card.

```html
<!DOCTYPE html>
<html lang="en">
<head>
<meta charset="utf-8">
<title>Maple Bridge Online – Business Card</title>
<link rel="stylesheet" href="https://fonts.googleapis.com/css2?family=Montserrat:wght@400;500&family=Lato:wght@400&display=swap">
<style>
  :root {
    --backdrop: #2a2a2a;
    --card: #ececee;
    --teal: #17a6b4;
    --coral: #e15f5f;
    --grey: #7b7b7d;
    --text: #66666a;
    --rule: #bdbdc0;
  }
  html, body {
    margin: 0;
    padding: 0;
    width: 1200px;
    height: 1200px;
    overflow: hidden;
    background: var(--backdrop);
  }
  .card {
    position: absolute;
    left: 180px;
    width: 840px;
    height: 480px;
    background: var(--card);
    box-shadow: 0 10px 24px rgba(0,0,0,0.45);
  }
  .card--front { top: 80px; }
  .card--back { top: 640px; }

  .tagline {
    position: absolute;
    right: 45px;
    top: 56px;
    margin: 0;
    font-family: "Montserrat", sans-serif;
    font-weight: 500;
    font-size: 25px;
    color: var(--grey);
    letter-spacing: 0.3px;
  }
  .front-brand {
    position: absolute;
    left: 56px;
    bottom: 70px;
    display: flex;
    align-items: center;
    gap: 22px;
  }
  .front-brand__dot {
    width: 56px;
    height: 56px;
    border-radius: 50%;
    background: var(--coral);
  }
  .front-brand__name {
    margin: 0;
    font-family: "Montserrat", sans-serif;
    font-weight: 500;
    font-size: 46px;
    color: var(--teal);
    line-height: 1.1;
  }

  .back-brand {
    position: absolute;
    left: 96px;
    top: 190px;
    width: 300px;
    text-align: center;
  }
  .back-brand__dot {
    width: 40px;
    height: 40px;
    margin: 0 auto 22px;
    border-radius: 50%;
    background: var(--coral);
  }
  .back-brand__name {
    margin: 0;
    font-family: "Lato", sans-serif;
    font-size: 30px;
    color: var(--teal);
    white-space: nowrap;
  }

  .contact {
    position: absolute;
    left: 438px;
    top: 108px;
    width: 330px;
    font-family: "Lato", sans-serif;
    color: var(--text);
  }
  .contact__name {
    margin: 0;
    font-family: "Montserrat", sans-serif;
    font-weight: 500;
    font-size: 33px;
    line-height: 1.1;
    color: var(--grey);
  }
  .contact__name .first { color: var(--teal); }
  .contact__role {
    margin: 4px 0 0;
    font-size: 18px;
  }
  .contact__rule {
    border: 0;
    border-top: 1px solid var(--rule);
    width: 300px;
    margin: 18px 0 14px;
  }
  .contact__address {
    margin: 0;
    font-style: normal;
    font-size: 18px;
    line-height: 26px;
  }
  .contact__list {
    list-style: none;
    margin: 0;
    padding: 0;
    font-size: 18px;
    line-height: 28px;
  }
  .contact__list li {
    display: flex;
    align-items: center;
    gap: 5px;
  }
  .contact__list svg { width: 14px; height: 14px; flex: none; }
</style>
</head>
<body>
  <section class="card card--front">
    <p class="tagline">For Mandarin Learning</p>
    <div class="front-brand">
      <span class="front-brand__dot"></span>
      <p class="front-brand__name">Maple Bridge Online</p>
    </div>
  </section>

  <section class="card card--back">
    <div class="back-brand">
      <div class="back-brand__dot"></div>
      <p class="back-brand__name">Maple Bridge Online</p>
    </div>

    <div class="contact">
      <h1 class="contact__name"><span class="first">Daniel</span> Reyes</h1>
      <p class="contact__role">Co-Founder | Partner</p>
      <hr class="contact__rule">
      <address class="contact__address">your street / Road, Suite 200<br>your country name</address>
      <hr class="contact__rule">
      <ul class="contact__list">
        <li>
          <svg viewBox="0 0 14 14" aria-hidden="true"><path fill="#17a6b4" d="M3 1l2.3 2.8-1.2 1.6c.8 1.8 2.2 3.3 4 4.2l1.6-1.2L13 10.6 11.4 13C6 12.6 1.4 8 1 2.6z"/></svg>
          <span>+65 555-0142</span>
        </li>
        <li>
          <svg viewBox="0 0 14 14" aria-hidden="true"><rect x="0.5" y="3" width="13" height="9" fill="#e15f5f"/><path d="M0.5 3l6.5 5 6.5-5" fill="none" stroke="#ececee" stroke-width="1.2"/></svg>
          <span>support@MapleBridgeOnline.com</span>
        </li>
        <li>
          <svg viewBox="0 0 14 14" aria-hidden="true"><g fill="none" stroke="#17a6b4" stroke-width="1.1"><circle cx="7" cy="7" r="6"/><ellipse cx="7" cy="7" rx="2.6" ry="6"/><path d="M1 7h12M2 4h10M2 10h10"/></g></svg>
          <span>www.maplebridgeonline.com</span>
        </li>
      </ul>
    </div>
  </section>
</body>
</html>
```